Australian IT Company New Logo Business Cards Required

We are a computer consultancy / MSP located in Brisbane Australia looking to have business cards designed with our new logo, we are looking for something professional that catches the eye.
I can provide the logo in other formats if required, let's see what you can create!

```html
<!DOCTYPE html>
<html lang="en">
<head>
<meta charset="utf-8">
<title>Varoleen Business Cards</title>
<link rel="stylesheet" href="https://fonts.googleapis.com/css2?family=Montserrat:wght@400;500;600;800&display=swap">
<style>
  :root {
    --bg: #c9c9c9;
    --green-light: #8ee02a;
    --green-dark: #68c40a;
    --ink: #1f2a12;
    --white: #ffffff;
    --card-black: #2b2b2b;
    --card-black-deep: #1c1c1c;
    --brand-green: #8bd822;
    --tagline-grey: #8a8a8a;
  }
  * { margin: 0; padding: 0; box-sizing: border-box; }
  html, body { width: 1200px; height: 675px; overflow: hidden; }
  body {
    background: var(--bg);
    font-family: "Montserrat", sans-serif;
    display: flex;
    align-items: center;
    justify-content: center;
    gap: 60px;
  }
  .card {
    position: relative;
    width: 500px;
    height: 286px;
    border-radius: 18px;
    box-shadow: 0 14px 30px rgba(0,0,0,0.22);
  }
  .card-front {
    background: linear-gradient(135deg, var(--green-light), var(--green-dark));
    color: var(--ink);
  }
  .card-back {
    background: linear-gradient(160deg, var(--card-black), var(--card-black-deep));
    display: flex;
    align-items: center;
    justify-content: center;
  }
  .brand { display: flex; flex-direction: column; }
  .brand-name {
    font-weight: 800;
    font-size: 36px;
    letter-spacing: 1px;
    line-height: 1;
  }
  .brand-tagline {
    font-weight: 600;
    font-size: 9.5px;
    letter-spacing: 0.6px;
    margin-top: 4px;
    text-transform: uppercase;
  }
  .card-front .brand { position: absolute; left: 34px; top: 48px; }
  .card-front .brand-name { color: var(--white); }
  .card-front .brand-tagline { color: var(--ink); }
  .card-back .brand { align-items: flex-start; }
  .card-back .brand-name { color: var(--brand-green); font-size: 42px; }
  .card-back .brand-tagline { color: var(--tagline-grey); font-size: 10.5px; }

  .holder { position: absolute; right: 44px; top: 82px; }
  .holder-name { font-weight: 600; font-size: 22px; color: #2d3a1c; line-height: 1; }
  .holder-role { font-weight: 500; font-size: 12px; color: var(--white); margin-top: 2px; }

  .contact {
    position: absolute;
    display: flex;
    align-items: center;
    gap: 10px;
    font-size: 12.5px;
    font-weight: 500;
    line-height: 1.55;
  }
  .contact-icons { display: flex; flex-direction: column; gap: 4px; }
  .contact-divider { width: 1px; align-self: stretch; background: var(--ink); }
  .contact-address { left: 34px; bottom: 58px; }
  .contact-reach { right: 60px; bottom: 26px; }
  .icon { width: 16px; height: 16px; display: block; }
</style>
</head>
<body>
  <section class="card card-front">
    <div class="brand">
      <span class="brand-name">VAROLEEN</span>
      <span class="brand-tagline">IT Solutions for Small Business</span>
    </div>
    <div class="holder">
      <div class="holder-name">NAME</div>
      <div class="holder-role">Designation</div>
    </div>
    <div class="contact contact-address">
      <div class="contact-icons">
        <svg class="icon" viewBox="0 0 16 16" aria-hidden="true">
          <path d="M8 1a4.5 4.5 0 0 0-4.5 4.5C3.5 9 8 13 8 13s4.5-4 4.5-7.5A4.5 4.5 0 0 0 8 1z" fill="var(--white)"/>
          <circle cx="8" cy="5.5" r="1.7" fill="var(--green-dark)"/>
          <ellipse cx="8" cy="14" rx="5" ry="1.3" fill="none" stroke="var(--white)" stroke-width="1"/>
        </svg>
      </div>
      <span class="contact-divider"></span>
      <div>Steet Name,<br>Zip Code &amp; Town</div>
    </div>
    <div class="contact contact-reach">
      <div class="contact-icons">
        <svg class="icon" viewBox="0 0 16 16" aria-hidden="true">
          <rect x="2" y="4" width="12" height="8.5" rx="1" fill="var(--white)"/>
          <path d="M2.5 4.5 8 9l5.5-4.5" fill="none" stroke="var(--green-dark)" stroke-width="1.2"/>
        </svg>
        <svg class="icon" viewBox="0 0 16 16" aria-hidden="true">
          <path d="M2 6c0-2 3-3 6-3s6 1 6 3l-2.5 1-1-1.5h-5l-1 1.5z" fill="var(--white)"/>
          <rect x="4.5" y="8" width="7" height="5" rx="1" fill="var(--white)"/>
        </svg>
      </div>
      <span class="contact-divider"></span>
      <div>Email ID<br>Phone No.</div>
    </div>
  </section>

  <section class="card card-back">
    <div class="brand">
      <span class="brand-name">VAROLEEN</span>
      <span class="brand-tagline">IT Solutions for Small Business</span>
    </div>
  </section>
</body>
</html>
```